UI design for kiosk touch screen

We need a UI design for a touch screen device to be used by costumers in a store and show information about specific products. We're looking for a general concept to serve as a starting point and we're not expecting a fully coded design.
We envision a UI where it first shows a range of products; once touched, it should show information about the product which includes text, touchable photos, videos and document files. We're interested in the starting page and the product details page.
We are the suppliers of the device and not the owners of stores that will use them. The purpose of this design is for in-person demonstrations to potential clients or in ads so the design should be agnostic about the end product(s). You may freely pick random placeholder or fictional products and assets to showcase the design concept as long as they can be changed without compromising the design. You can use our logo (annexed) in the design as a placeholder but it's not necessary.
We're using web technologies to develop the UI so the same principles should apply, except some exceptions below:
- There's no need for a responsive design since the resolution is set at 1920x1080 on a 22'' monitor in landscape orientation.
- All interactions will be done using the touchscreen, so any interactive component needs to be large enough for navigation to be comfortable.
- The design should be visually engaging and eye-catching, more so than a regular website.
Physical shop owners.
Store
2 page

```html
<!DOCTYPE html>
<html lang="en">
<head>
<meta charset="utf-8">
<title>Kiosk UI Design V1</title>
<link href="https://fonts.googleapis.com/css2?family=Open+Sans:wght@300;400;600;700&display=swap" rel="stylesheet">
<style>
:root{
  --blue:#2288F6;
  --ink:#2F323B;
  --grey:#CBCED6;
  --white:#FFFFFF;
  --muted:#8A8E98;
  --line:#E6E8EC;
  --star:#F5A623;
}
*{box-sizing:border-box;margin:0;padding:0}
html,body{width:1200px;height:1200px;overflow:hidden;background:var(--white)}
body{position:relative;font-family:"Open Sans",Arial,sans-serif;color:var(--ink)}
.headline{position:absolute;top:58px;left:0;width:1200px;text-align:center;font-size:108px;font-weight:400;letter-spacing:1px;line-height:1.2}
.screen{position:absolute;width:560px;height:315px;background:var(--white);box-shadow:0 3px 10px rgba(0,0,0,.16);overflow:hidden}
.s-home{left:33px;top:277px}
.s-detail{left:608px;top:277px}
.s-grid{left:33px;top:608px}
.s-tiles{left:608px;top:608px}

/* home */
.hero{position:absolute;left:0;top:0;width:360px;height:315px;background:linear-gradient(135deg,#3c4048 0%,#8b7b62 45%,#c9b48c 70%,#5a5f68 100%)}
.brand-block{position:absolute;left:40px;top:28px;display:flex;align-items:center;gap:12px;color:var(--white)}
.brand-mark{width:56px;height:56px;background:var(--white)}
.brand-name{font-size:44px;font-weight:700;line-height:1;letter-spacing:1px}
.brand-tag{position:absolute;left:108px;top:75px;font-size:7px;font-weight:600;color:var(--white);letter-spacing:.3px}
.hero-claim{position:absolute;left:38px;top:266px;color:var(--white);font-size:7.5px;font-weight:600;line-height:1.25}
.hero-note{position:absolute;left:38px;top:292px;color:#e8e8e8;font-size:4px;line-height:1.3}
.hero-next{position:absolute;left:302px;top:268px;width:22px;height:22px;border:1.5px solid var(--white);border-radius:50%}
.menu{position:absolute;left:360px;top:0;width:200px;height:315px;background:var(--white)}
.menu-item{height:73px;border-bottom:1px solid var(--line);display:flex;align-items:center;justify-content:space-between;padding:0 40px 0 37px;font-size:14.5px;position:relative}
.menu-item.active::after{content:"";position:absolute;right:0;top:0;width:3px;height:100%;background:var(--blue)}
.menu-foot{position:absolute;left:0;bottom:6px;width:200px;text-align:center;font-size:4px;color:var(--muted);line-height:1.4}

/* bar */
.bar{position:absolute;left:0;top:0;width:100%;height:25px;background:var(--ink);display:flex;align-items:center;justify-content:space-between;padding:0 12px}
.bar-tools{display:flex;gap:18px;align-items:center}
.substrip{position:absolute;left:0;top:25px;width:100%;height:14px;border-bottom:1px solid var(--line);font-size:5px;color:#a9adb5;padding:4px 6px;display:flex;justify-content:space-between;background:var(--white);z-index:2}

/* detail */
.detail-photo{position:absolute;left:20px;top:70px;width:270px;height:150px;border-radius:6px;background:linear-gradient(180deg,#3a3e47 0%,#1d1f25 55%,#c98aa0 80%,#e9c36a 100%)}
.divider-v{position:absolute;left:315px;top:43px;width:1px;height:272px;background:var(--line)}
.fav-btn{position:absolute;left:22px;top:253px;width:44px;height:44px;border-radius:50%;background:var(--white);box-shadow:0 1px 5px rgba(0,0,0,.2);display:flex;align-items:center;justify-content:center}
.d-info{position:absolute;left:328px;top:55px;width:220px}
.d-title{display:flex;gap:14px;align-items:baseline;font-size:17px}
.d-brand{color:var(--blue);font-weight:700;font-size:15px}
.d-sub{font-size:11.5px;color:var(--muted);margin-top:2px}
.d-text{font-size:11.5px;color:var(--muted);line-height:1.45;font-weight:300}
.d-meta{display:flex;justify-content:space-between;align-items:center;margin-top:14px;padding:0 6px}
.d-rate{font-size:14px}
.d-rate span{color:var(--star);font-size:14px}
.d-price{color:var(--blue);font-size:18px}
.d-specs{position:absolute;left:328px;top:207px;width:225px;border-top:1px solid var(--line);padding-top:8px}
.d-specs h4{font-size:8.5px;font-weight:400;color:var(--muted);margin-bottom:6px}
.spec-cols{display:grid;grid-template-columns:110px 115px;row-gap:8.5px;font-size:6.5px;color:var(--muted)}
.dropdown{position:absolute;left:472px;top:13px;width:72px;background:var(--white);box-shadow:0 2px 6px rgba(0,0,0,.2);padding:3px 0;z-index:5}
.dropdown div{font-size:9px;padding:4px 7px;height:20.5px}

/* grid list */
.list-clip{position:absolute;left:0;top:40px;width:100%;height:275px;overflow:hidden}
.list{position:absolute;left:0;top:-40px;width:100%;display:grid;grid-template-columns:repeat(3,1fr)}
.card{height:105px;border-right:1px solid var(--line);border-bottom:1px solid var(--line);position:relative}
.card.selected{outline:1px solid var(--blue);outline-offset:-1px}
.card .thumb{position:absolute;left:14px;top:32px;width:82px;height:44px;border-radius:4px;background:linear-gradient(180deg,#d9dbe0,#9fa3ab)}
.thumb.dark{background:linear-gradient(180deg,#4a4e57,#1c1e23)}
.thumb.photo{background:linear-gradient(180deg,#30333b 0%,#1c1e23 60%,#d48aa3 80%,#eac76b 100%)}
.card .txt{position:absolute;left:111px;top:12px;width:75px}
.brand{font-size:10px;font-weight:700;color:var(--ink);height:13px}
.name{font-size:11.5px;line-height:1.25}
.desc{font-size:7px;color:var(--muted);line-height:1.5}
.price{font-size:10px;color:var(--blue);margin-top:7px}
.rating{font-size:8px;margin-top:9px}
.rating span{color:var(--star)}
.heart-mini{position:absolute;left:46px;top:78px;width:18px;height:18px;border-radius:50%;box-shadow:0 1px 3px rgba(0,0,0,.2);background:var(--white)}

/* tiles */
.tiles{position:absolute;left:0;top:-75px;width:100%;display:grid;grid-template-columns:repeat(4,1fr)}
.tile{height:175px;border-right:1px solid var(--line);border-bottom:1px solid var(--line);position:relative}
.tile.selected{outline:1px solid var(--blue);outline-offset:-1px}
.tile .brand{position:absolute;left:22px;top:14px}
.tile .thumb{position:absolute;left:18px;top:40px;width:104px;height:62px;border-radius:4px;background:linear-gradient(180deg,#d9dbe0,#9fa3ab)}
.tile .row{position:absolute;left:21px;top:137px;width:110px;display:flex;justify-content:space-between;align-items:baseline;font-size:11px}
.tile .row .price{margin:0}
.tile .rating{position:absolute;left:21px;top:153px;margin:0}
.tile .heart-mini{left:22px;top:113px}

/* palette */
.swatch{position:absolute;top:998px;width:98px;height:98px;border-radius:50%}
.swatch.w{box-shadow:0 1px 5px rgba(0,0,0,.12)}
.hex{position:absolute;top:1120px;width:140px;text-align:center;font-size:21px;color:#444}
</style>
</head>
<body>

<h1 class="headline">UI Design V1</h1>

<!-- Home screen -->
<section class="screen s-home">
  <div class="hero" role="img" aria-label="Photo of a business handshake in a bright office"></div>
  <div class="brand-block"><div class="brand-mark"></div><div class="brand-name">NORVAL</div></div>
  <div class="brand-tag">DIGITAL RETAIL SYSTEMS</div>
  <div class="hero-claim">THE RIGHT SOLUTION<br>FOR A BETTER BUSINESS.</div>
  <div class="hero-note">ALL CATALOGUE PRICES ARE MAXIMUM PRICES VALID UNTIL 30 JULY 2017<br>PRICES ARE SUBJECT TO ANY ALTERATION IN VAT</div>
  <div class="hero-next"><svg width="19" height="19" viewBox="0 0 20 20"><path d="M8 6l4 4-4 4" fill="none" stroke="#fff" stroke-width="1.5"/></svg></div>
  <nav class="menu">
    <div class="menu-item">Catalogue
      <svg width="24" height="28" viewBox="0 0 24 28"><path d="M3 2h13l5 5v19H3z" fill="none" stroke="#2F323B" stroke-width="1.2"/><path d="M7 10h10M7 14h10M7 18h10M7 22h10" stroke="#2F323B" stroke-width="1"/></svg></div>
    <div class="menu-item active">Favourites
      <svg width="28" height="26" viewBox="0 0 28 26"><path d="M14 24C4 16 1 12 1 7.5 1 4 4 1 7.5 1 10.5 1 13 3 14 5c1-2 3.5-4 6.5-4C24 1 27 4 27 7.5 27 12 24 16 14 24z" fill="none" stroke="#2288F6" stroke-width="1.4"/></svg></div>
    <div class="menu-item">Settings
      <svg width="30" height="30" viewBox="0 0 30 30"><circle cx="15" cy="15" r="11" fill="none" stroke="#2F323B" stroke-width="4" stroke-dasharray="4 3.2"/><circle cx="15" cy="15" r="8.5" fill="#fff" stroke="#2F323B" stroke-width="1.2"/><circle cx="15" cy="15" r="4.5" fill="none" stroke="#2F323B" stroke-width="1.2"/></svg></div>
    <div class="menu-item">Help
      <svg width="28" height="28" viewBox="0 0 28 28"><circle cx="14" cy="14" r="13" fill="none" stroke="#2F323B" stroke-width="1.2"/><path d="M10.5 10.5a3.5 3.5 0 1 1 5 3.2c-1 .5-1.5 1.3-1.5 2.5v1" fill="none" stroke="#2F323B" stroke-width="1.3"/><circle cx="14" cy="20.5" r=".9" fill="#2F323B"/></svg></div>
    <div class="menu-foot">© Norval Systems 2017<br>Terms of use | Privacy Policy</div>
  </nav>
</section>

<!-- Product detail screen -->
<section class="screen s-detail">
  <div class="bar">
    <svg width="14" height="12" viewBox="0 0 14 12"><path d="M13 6H1M6 1L1 6l5 5" fill="none" stroke="#fff" stroke-width="1.2"/></svg>
    <div class="bar-tools">
      <svg width="11" height="11" viewBox="0 0 12 12"><circle cx="5" cy="5" r="4" fill="none" stroke="#fff" stroke-width="1.2"/><path d="M8 8l3.5 3.5" stroke="#fff" stroke-width="1.2"/></svg>
      <svg width="14" height="11" viewBox="0 0 14 11"><path d="M0 1h14M0 5.5h14M0 10h14" stroke="#fff" stroke-width="1.2"/></svg>
    </div>
  </div>
  <div class="substrip"><span>CATEGORY: PRINTERS | CORVO &nbsp; PRODUCT NAME: CORVO VISTA 640 ALL IN ONE</span><span>SHARE</span></div>
  <div class="dropdown"><div>Home</div><div>Catalogue</div><div>Favourites</div><div>Settings</div><div>Help</div></div>
  <div class="detail-photo" role="img" aria-label="Product photo of an all-in-one printer with a printed photo"></div>
  <div class="fav-btn"><svg width="24" height="22" viewBox="0 0 28 26"><path d="M14 24C4 16 1 12 1 7.5 1 4 4 1 7.5 1 10.5 1 13 3 14 5c1-2 3.5-4 6.5-4C24 1 27 4 27 7.5 27 12 24 16 14 24z" fill="none" stroke="#2288F6" stroke-width="1.6"/></svg></div>
  <div class="divider-v"></div>
  <div class="d-info">
    <div class="d-title">Vista 640 <span class="d-brand">CORVO</span></div>
    <div class="d-sub">Premium printer</div>
    <p class="d-text">ultra color Lorem ipsum dolor sit, consectetuer adipiscing elit. Aenean commodo ligula eget dolor.</p>
    <div class="d-meta"><div class="d-rate">4.1 <span>★★★★</span></div><div class="d-price">$ 79.99</div></div>
  </div>
  <div class="d-specs">
    <h4>SPECIFICATIONS :</h4>
    <div class="spec-cols">
      <div>Print color - Color</div><div>Print services - Cloud, Mobile</div>
      <div>Type - Inkjet</div><div>Number of cartridges - 4x</div>
      <div>Scanning to - Email, PC</div><div>Paper feed - Charge</div>
      <div>Wifi - Onboard</div><div>Connection - USB 2.0</div>
      <div>Paper format - A4, A5, A6, B5</div><div>Scan resolution - 1200, 2400 dpi</div>
    </div>
  </div>
</section>

<!-- Catalogue list screen -->
<section class="screen s-grid">
  <div class="bar">
    <svg width="14" height="12" viewBox="0 0 14 12"><path d="M13 6H1M6 1L1 6l5 5" fill="none" stroke="#fff" stroke-width="1.2"/></svg>
    <div class="bar-tools">
      <svg width="11" height="11" viewBox="0 0 12 12"><circle cx="5" cy="5" r="4" fill="none" stroke="#fff" stroke-width="1.2"/><path d="M8 8l3.5 3.5" stroke="#fff" stroke-width="1.2"/></svg>
      <svg width="14" height="11" viewBox="0 0 14 11"><path d="M0 1h14M0 5.5h14M0 10h14" stroke="#fff" stroke-width="1.2"/></svg>
    </div>
  </div>
  <div class="substrip"><span>RESULT : 1028</span><span>▦ &nbsp; ▼ FILTER</span></div>
  <div class="list-clip"><div class="list">
    <div class="card"><div class="thumb" role="img" aria-label="Laser printer"></div><div class="txt"><div class="brand">HANEUL</div><div class="name">BRN XP2.0</div><div class="desc">Photo changer<br>99% color safer...</div><div class="price">$ 159.99</div><div class="rating">4.7 <span>★★★★★</span></div></div></div>
    <div class="card"><div class="thumb dark" role="img" aria-label="Laser printer"></div><div class="txt"><div class="brand">LUMEN</div><div class="name">Orbit 1425</div><div class="desc">Laser printer<br>6 correction mods...</div><div class="price">$ 199.99</div><div class="rating">4.5 <span>★★★★★</span></div></div></div>
    <div class="card"><div class="thumb dark" role="img" aria-label="Laser printer"></div><div class="txt"><div class="brand">LUMEN</div><div class="name">Orbit 1425</div><div class="desc">Laser printer<br>3 correction mods...</div><div class="price">$ 162.99</div><div class="rating">4.9 <span>★★★★★</span></div></div></div>

    <div class="card"><div class="thumb dark" role="img" aria-label="Multifunction printer"></div><div class="txt"><div class="brand">LUMEN</div><div class="name">Orbit 2490</div><div class="desc">Laser printer<br>6 correction mods...</div><div class="price">$ 199.99</div><div class="rating">4.5 <span>★★★★★</span></div></div></div>
    <div class="card selected"><div class="thumb dark" role="img" aria-label="Laser printer"></div><div class="heart-mini"></div><div class="txt"><div class="brand">LUMEN</div><div class="name">Orbit 1425</div><div class="desc">Laser printer<br>3 correction mods...</div><div class="price">$ 162.99</div><div class="rating">4.9 <span>★★★★★</span></div></div></div>
    <div class="card"><div class="thumb photo" role="img" aria-label="Photo printer"></div><div class="txt"><div class="brand">CORVO</div><div class="name">Vista 640</div><div class="desc">Premium printer<br>ultra color...</div><div class="price">$ 79.99</div><div class="rating">4.1 <span>★★★★</span></div></div></div>

    <div class="card"><div class="thumb" role="img" aria-label="Laser printer"></div><div class="txt"><div class="brand">HANEUL</div><div class="name">BRN XP1.0</div><div class="desc">Mega laser<br>photo print...</div><div class="price">$ 299.99</div><div class="rating">3.9 <span>★★★★</span></div></div></div>
    <div class="card"><div class="thumb photo" role="img" aria-label="Photo printer"></div><div class="txt"><div class="brand">CORVO</div><div class="name">Vista 640</div><div class="desc">Premium printer<br>ultra color...</div><div class="price">$ 79.99</div><div class="rating">4.1 <span>★★★★</span></div></div></div>
    <div class="card"><div class="thumb" role="img" aria-label="Laser printer"></div><div class="txt"><div class="brand">HANEUL</div><div class="name">BRN XP2.0</div><div class="desc">Photo changer<br>99% color safer...</div><div class="price">$ 159.99</div><div class="rating">4.7 <span>★★★★★</span></div></div></div>
  </div></div>
</section>

<!-- Catalogue tile screen -->
<section class="screen s-tiles">
  <div class="bar">
    <svg width="14" height="12" viewBox="0 0 14 12"><path d="M13 6H1M6 1L1 6l5 5" fill="none" stroke="#fff" stroke-width="1.2"/></svg>
    <div class="bar-tools">
      <svg width="11" height="11" viewBox="0 0 12 12"><circle cx="5" cy="5" r="4" fill="none" stroke="#fff" stroke-width="1.2"/><path d="M8 8l3.5 3.5" stroke="#fff" stroke-width="1.2"/></svg>
      <svg width="14" height="11" viewBox="0 0 14 11"><path d="M0 1h14M0 5.5h14M0 10h14" stroke="#fff" stroke-width="1.2"/></svg>
    </div>
  </div>
  <div class="substrip"><span>RESULT : 1028</span><span>▦ &nbsp; ▼ FILTER</span></div>
  <div class="list-clip"><div class="tiles">
    <div class="tile"><div class="brand">LUMEN</div><div class="thumb dark" role="img" aria-label="Laser printer"></div><div class="row"><span>Orbit 1425</span><span class="price">$ 162.99</span></div><div class="rating">3.9 <span>★★★★</span></div></div>
    <div class="tile"><div class="brand">CORVO</div><div class="thumb photo" role="img" aria-label="Photo printer"></div><div class="row"><span>Vista 640</span><span class="price">$ 159.99</span></div><div class="rating">4.9 <span>★★★★★</span></div></div>
    <div class="tile"><div class="brand">HANEUL</div><div class="thumb" role="img" aria-label="Laser printer"></div><div class="row"><span>BRN XP2.0</span><span class="price">$ 299.99</span></div><div class="rating">4.1 <span>★★★★</span></div></div>
    <div class="tile"><div class="brand">LUMEN</div><div class="thumb dark" role="img" aria-label="Laser printer"></div><div class="row"><span>Vista 640</span><span class="price">$ 79.99</span></div><div class="rating">4.7 <span>★★★★★</span></div></div>

    <div class="tile selected"><div class="brand">LUMEN</div><div class="thumb dark" role="img" aria-label="Multifunction printer"></div><div class="heart-mini"></div><div class="row"><span>Vista 640</span><span class="price">$ 79.99</span></div><div class="rating">4.7 <span>★★★★★</span></div></div>
    <div class="tile"><div class="brand">HANEUL</div><div class="thumb" role="img" aria-label="Laser printer"></div><div class="row"><span>BRN XP2.0</span><span class="price">$ 299.99</span></div><div class="rating">4.1 <span>★★★★</span></div></div>
    <div class="tile"><div class="brand">LUMEN</div><div class="thumb dark" role="img" aria-label="Laser printer"></div><div class="row"><span>Orbit 1425</span><span class="price">$ 162.99</span></div><div class="rating">3.9 <span>★★★★</span></div></div>
    <div class="tile"><div class="brand">CORVO</div><div class="thumb photo" role="img" aria-label="Photo printer"></div><div class="row"><span>Vista 640</span><span class="price">$ 159.99</span></div><div class="rating">4.9 <span>★★★★★</span></div></div>
  </div></div>
</section>

<!-- Palette -->
<div class="swatch" style="left:351px;background:var(--blue)"></div>
<div class="swatch" style="left:484px;background:var(--ink)"></div>
<div class="swatch" style="left:617px;background:var(--grey)"></div>
<div class="swatch w" style="left:750px;background:var(--white)"></div>
<div class="hex" style="left:330px">#2288F6</div>
<div class="hex" style="left:463px">#2F323B</div>
<div class="hex" style="left:599px">#CBCED6</div>
<div class="hex" style="left:735px">#FFFFFF</div>

</body>
</html>
```